Time for a better IT consulting company?

We are a mobile computer consulting company, taking care of client's issues remotely or at their site. Website of company www.qr-lumotek.com. Business card is an example of marketing so far.
We moved this year but we still service our existing clients. We have expanded our number of technicians available. We would like to use this card for both new business and reaching out to old business.

Target Market(s)

This should target businesses and referrals to businesses from our existing clients as well as a new client outreach for our new location.

Industry/Entity Type

Computer

Requirements
Must have
• This postcard will let clients know we have moved into or we continue to service their area. Make sure it says Inc, not LLC. Must incorporate existing theme in some fashion.
Nice to have
• Themes to communicate: team of people standing by, stability, faster response time, accessibility.
• Areas of coverage: Westchester, Rockland, Manhattan, The Bronx, lower Connecticut.
Should not have
• Cartoon feel.

```html
<!DOCTYPE html>
<html lang="en">
<head>
<meta charset="utf-8">
<title>Kestrel Point Computer Consulting Inc – Card</title>
<link rel="stylesheet" href="https://fonts.googleapis.com/css2?family=Open+Sans:wght@400;600&family=Tinos&display=swap">
<style>
  :root {
    --page: #e9e9e9;
    --card-dark: #3b3d40;
    --card-darker: #1f2023;
    --band: #4a4b4e;
    --accent: #4d97ad;
    --accent-soft: #6fb1c4;
    --text-light: #f2f2f2;
    --text-muted: #cfd3d6;
    --name-grey: #6b6e72;
  }
  * { margin: 0; padding: 0; box-sizing: border-box; }
  html, body { width: 1200px; height: 856px; overflow: hidden; background: var(--page); }
  .card {
    position: absolute; left: 100px; top: 78px; width: 1000px; height: 700px;
    background: linear-gradient(160deg, var(--card-dark) 0%, #2c2d30 55%, var(--card-darker) 100%);
    overflow: hidden; box-shadow: 0 6px 22px rgba(0,0,0,.25);
    font-family: "Tinos", "Times New Roman", serif; color: var(--text-light);
  }
  .card-shapes { position: absolute; inset: 0; }
  .hero-visual {
    position: absolute; left: 330px; top: 250px; width: 670px; height: 330px;
    background:
      radial-gradient(ellipse at 62% 40%, rgba(230,240,255,.85) 0%, rgba(120,180,220,.55) 18%, rgba(40,90,140,.35) 42%, transparent 68%),
      radial-gradient(ellipse at 60% 78%, rgba(190,120,150,.45) 0%, transparent 45%),
      linear-gradient(120deg, #1c2b3c 0%, #25496a 50%, #1a2735 100%);
    clip-path: polygon(12% 0, 100% 0, 100% 100%, 0 100%);
    opacity: .95;
  }
  .brand {
    position: absolute; left: 36px; top: 122px; display: flex; align-items: center; gap: 12px;
    font-family: "Open Sans", Arial, sans-serif; font-weight: 600; color: var(--name-grey);
  }
  .brand-dot { width: 50px; height: 50px; border-radius: 50%; background: var(--name-grey); flex: none; }
  .brand-name { font-size: 20px; line-height: 1.2; letter-spacing: .5px; }
  .brand-name small { display: block; font-size: 10px; letter-spacing: 1px; }
  .phone {
    position: absolute; left: 400px; top: 52px; display: flex; align-items: center; gap: 14px;
    font-size: 56px; letter-spacing: .5px;
  }
  .phone svg { width: 50px; height: 50px; flex: none; }
  .tagline {
    position: absolute; left: 40px; top: 356px; width: 340px; font-size: 20px; line-height: 1.3; color: var(--text-muted);
  }
  .coverage {
    position: absolute; left: 40px; top: 440px; width: 300px; font-size: 17px; line-height: 1.5; color: var(--text-muted);
  }
  .coverage strong { display: block; font-weight: 400; font-size: 19px; color: var(--text-light); margin-bottom: 6px; }
  .services {
    position: absolute; left: 380px; top: 420px; width: 380px; list-style: none;
    font-size: 20px; line-height: 1.55; color: var(--text-light);
  }
  .services li { position: relative; padding-left: 22px; }
  .services li::before {
    content: ""; position: absolute; left: 2px; top: 11px;
    border-left: 8px solid var(--text-muted); border-top: 5px solid transparent; border-bottom: 5px solid transparent;
  }
  .contact {
    position: absolute; right: 40px; top: 330px; text-align: right; font-size: 15px; line-height: 1.5; color: var(--text-muted);
  }
  .contact h2 {
    font-family: "Open Sans", Arial, sans-serif; font-weight: 600; font-size: 27px; color: var(--text-light); line-height: 1.2;
  }
</style>
</head>
<body>
<main class="card">
  <svg class="card-shapes" viewBox="0 0 1000 700" aria-hidden="true">
    <defs>
      <linearGradient id="light-panel" x1="0" y1="0" x2="1" y2="1">
        <stop offset="0" stop-color="#f4f4f4"/><stop offset="1" stop-color="#d9d9d9"/>
      </linearGradient>
      <linearGradient id="sheen" x1="0" y1="0" x2="0" y2="1">
        <stop offset="0" stop-color="#fff" stop-opacity=".08"/><stop offset="1" stop-color="#fff" stop-opacity="0"/>
      </linearGradient>
    </defs>
    <polygon points="0,0 320,0 250,320 0,320" fill="url(#light-panel)"/>
    <polygon points="0,320 250,320 330,250 380,250 360,340 0,400" fill="var(--band)"/>
    <polygon points="0,400 360,340 330,700 0,700" fill="url(#sheen)"/>
    <circle cx="1000" cy="70" r="130" fill="var(--accent)" opacity=".75"/>
    <circle cx="1010" cy="60" r="90" fill="var(--accent-soft)" opacity=".35"/>
  </svg>

  <div class="hero-visual" role="img" aria-label="Photo of a hand holding a glowing globe with network and email icons over a laptop"></div>

  <div class="brand">
    <span class="brand-dot"></span>
    <p class="brand-name">KESTREL POINT<small>COMPUTER CONSULTING INC</small></p>
  </div>

  <p class="phone">
    <svg viewBox="0 0 50 50" aria-hidden="true">
      <circle cx="25" cy="25" r="22" fill="none" stroke="currentColor" stroke-width="3"/>
      <path d="M17 14c2-1 3 0 4 2l2 4c1 2 0 3-1 4 1 3 3 5 6 6 1-1 2-2 4-1l4 2c2 1 3 2 2 4-2 3-5 4-8 3-7-2-12-7-14-14-1-3 0-8 1-10z" fill="currentColor"/>
    </svg>
    914-555-0182
  </p>

  <p class="tagline">Need immediate assistance with a computer issue?</p>

  <div class="coverage">
    <strong>We've moved – and we still serve you.</strong>
    <p>More technicians standing by for faster on-site response across Westchester, Rockland, Manhattan, The Bronx and Lower Connecticut.</p>
  </div>

  <ul class="services">
    <li>We offer on-site business &amp; residential service &amp; repair including: emergency services, IT staffing, IP phones,</li>
    <li>hardware/software, security reviews, and web development for Mac and PC.</li>
  </ul>

  <div class="contact">
    <h2>Contact Us</h2>
    <p>Kestrel Point Computer Consulting Inc</p>
    <p>info@qr-lumotek.com</p>
    <p>www.qr-lumotek.com</p>
  </div>
</main>
</body>
</html>
```